Design some Business Cards for Jewelry Company

Hello All!

We would like to create business cards for our company: Velk Sisters

We manufacture jewelry.

We will be using Quickfern [login to view URL] to print our cards
See here for print specs & size template: [login to view URL]

Attached is our logo file.

Our business card info (will provide later, but use the below for now):
Name: Marcus Pell
Title: Managing Partner
Address: 487 N. Corrin Blvd. Suite 2200C
Chicago, IL 60603
Phone #1: 800.555.0142
Phone #2: 312.555.0187
Fax #: 312.555.0163
Email: marcus@[login to view URL]
Web Site: [login to view URL]

Things we like, but also open to other ideas:
1) Incorporate QR code
2) Water mark with the design is very nice
3) Instead of putting "T" or "Tel" for telephone, I like the little small icon for phone, email, etc.
4) Sleek design

Good luck! I look forward to seeing all your great designs!

```html
<!DOCTYPE html>
<html lang="en">
<head>
<meta charset="utf-8">
<title>Velk Sisters Business Cards</title>
<link rel="stylesheet" href="https://fonts.googleapis.com/css2?family=Open+Sans:wght@400;600;700;800&display=swap">
<style>
  :root {
    --bg: #2b2b2d;
    --card-top: #ffffff;
    --card-bottom: #e6e6e6;
    --orange: #f08a1c;
    --orange-soft: #f6a54a;
    --ink: #4a4a4c;
    --ink-light: #6d6d70;
  }
  * { margin: 0; padding: 0; box-sizing: border-box; }
  html, body {
    width: 1200px; height: 901px; overflow: hidden;
    background: var(--bg);
    font-family: "Open Sans", sans-serif;
  }
  .stage { position: relative; width: 1200px; height: 901px; }
  .card {
    position: absolute; top: 307px;
    width: 500px; height: 286px;
    border-radius: 22px; overflow: hidden;
    background: linear-gradient(160deg, var(--card-top) 0%, var(--card-bottom) 100%);
  }
  .card--front { left: 60px; }
  .card--back { left: 640px; }

  .brand-dot {
    position: absolute; border-radius: 50%;
    background: linear-gradient(150deg, var(--orange-soft), var(--orange));
  }
  .card--front .brand-dot { left: 52px; top: 88px; width: 140px; height: 140px; }
  .card--back .brand-dot { left: 230px; top: 20px; width: 190px; height: 190px; }

  .brand-name {
    position: absolute; color: var(--ink);
    font-weight: 800; letter-spacing: 0.5px; white-space: nowrap;
  }
  .card--front .brand-name { left: 250px; top: 30px; font-size: 24px; }
  .card--back .brand-name { right: 34px; bottom: 34px; font-size: 32px; }

  .person { position: absolute; left: 250px; top: 78px; }
  .person__name { color: var(--orange); font-size: 20px; font-weight: 700; line-height: 1.2; }
  .person__title { color: var(--ink-light); font-size: 12px; font-weight: 400; margin-top: 2px; }
  .divider {
    position: absolute; left: 250px; top: 128px;
    width: 220px; height: 1px; background: var(--orange);
  }
  .contacts {
    position: absolute; left: 250px; top: 140px;
    list-style: none; color: var(--ink); font-size: 11px; line-height: 16px;
  }
  .contacts li { display: flex; align-items: flex-start; gap: 7px; }
  .contacts svg { width: 11px; height: 11px; margin-top: 2px; flex: none; }
</style>
</head>
<body>
<main class="stage">
  <section class="card card--front" aria-label="Business card front">
    <div class="brand-dot"></div>
    <div class="brand-name">VELK SISTERS</div>
    <div class="person">
      <div class="person__name">Marcus Pell</div>
      <div class="person__title">Managing Partner</div>
    </div>
    <div class="divider"></div>
    <ul class="contacts">
      <li>
        <svg viewBox="0 0 12 12"><path d="M6 1 L11 6 H9.5 V11 H7 V8 H5 V11 H2.5 V6 H1 Z" fill="#f08a1c"/></svg>
        <span>487 N. Corrin Blvd. Suite 2200C<br>Chicago, IL 60603</span>
      </li>
      <li>
        <svg viewBox="0 0 12 12"><path d="M3 1 L5 1 L5.8 3.6 L4.4 4.6 C5 6 6 7 7.4 7.6 L8.4 6.2 L11 7 L11 9 C11 10 10 11 9 11 C5 11 1 7 1 3 C1 2 2 1 3 1 Z" fill="#f08a1c"/></svg>
        <span>800.555.0142</span>
      </li>
      <li>
        <svg viewBox="0 0 12 12"><rect x="3" y="0.5" width="6" height="11" rx="1.2" fill="#f08a1c"/><rect x="4" y="2" width="4" height="6.5" fill="#fff"/></svg>
        <span>312.555.0187</span>
      </li>
      <li>
        <svg viewBox="0 0 12 12"><rect x="3" y="1" width="6" height="3.5" fill="#f08a1c"/><rect x="1" y="4.5" width="10" height="5" rx="1" fill="#f08a1c"/><rect x="3" y="8" width="6" height="3" fill="#f08a1c" stroke="#fff" stroke-width="0.8"/></svg>
        <span>312.555.0163</span>
      </li>
      <li>
        <svg viewBox="0 0 12 12"><rect x="0.5" y="2" width="11" height="8" rx="1" fill="#f08a1c"/><path d="M1 2.6 L6 6.6 L11 2.6" fill="none" stroke="#fff" stroke-width="1"/></svg>
        <span>marcus@velksisters.com</span>
      </li>
      <li>
        <svg viewBox="0 0 12 12"><circle cx="6" cy="6" r="5" fill="#f08a1c"/><path d="M1 6 H11 M6 1 C3.5 3.5 3.5 8.5 6 11 M6 1 C8.5 3.5 8.5 8.5 6 11" fill="none" stroke="#fff" stroke-width="0.7"/></svg>
        <span>www.velksisters.com</span>
      </li>
    </ul>
  </section>

  <section class="card card--back" aria-label="Business card back">
    <div class="brand-dot"></div>
    <div class="brand-name">VELK SISTERS</div>
  </section>
</main>
</body>
</html>
```